IT company requires website redesign

I have an old boring website that I want to update - www.tvkb-example.net
I am a growing IT company beginning to look after more healthcare professionals such as medical and dental practices so a more professional look is required

Blue and orange are the company colours. See one of our local competitors for your reference and ideas - https://www.plinth-halvard.example.au

Target Market(s)

Medical, dental, professional, solicitors etc

Industry/Entity Type

It Support

Number of Pages Required

5+ page

Colors

Designer to choose colors to be used in the design.

Requirements
Must have
• Classy feel, simple with the 'less is more' approach
• On support page, links to support items, a couple more to come
• Reference to our technology partners
• Easy to read
Nice to have
• Company colours are blue with a little orange but I willing to consider new web colour schemes
• leave the rest to you

```html
<!DOCTYPE html>
<html lang="en">
<head>
<meta charset="utf-8">
<title>Tidewell Systems – IT Support</title>
<link href="https://fonts.googleapis.com/css2?family=Raleway:wght@400;500;600;700&family=Open+Sans:wght@400;600;700&display=swap" rel="stylesheet">
<style>
:root{
  --orange:#f26a1b;
  --navy:#1f2a78;
  --navy-dark:#19226a;
  --ink:#222;
  --grey-bg:#f2f2f2;
  --dark:#1b1b1d;
  --white:#fff;
  --body:'Open Sans',Arial,sans-serif;
  --head:'Raleway',Arial,sans-serif;
}
*{box-sizing:border-box;margin:0;padding:0}
html,body{width:1200px;height:5357px;overflow:hidden}
body{font-family:var(--body);color:var(--ink);background:var(--white);position:relative}
section,header,footer{position:relative;width:1200px;overflow:hidden}
a{color:inherit;text-decoration:none}
.btn{display:inline-block;background:var(--navy);color:var(--white);border-radius:30px;font-size:17px;padding:14px 36px;font-family:var(--body)}

/* top bar */
.topbar{height:60px;background:var(--orange);color:var(--white);display:flex;align-items:center;padding:0 90px;font-size:15px;gap:64px}
.topbar .item{display:flex;align-items:center;gap:14px}
.topbar .social{margin-left:auto;display:flex;gap:8px}
.topbar .social span{width:22px;height:22px;background:var(--white);border-radius:3px}

/* header */
.site-header{height:180px;display:flex;align-items:center;padding:0 90px}
.brand{display:flex;align-items:center;gap:14px;font-family:var(--head);font-weight:700;font-size:30px;color:var(--navy)}
.brand .mark{width:26px;height:26px;background:var(--orange);border-radius:50%}
.nav{margin-left:auto;display:flex;gap:30px;font-size:16px;color:var(--orange)}

/* hero */
.hero{height:640px;background:linear-gradient(100deg,#7f93a4 0%,#b7c3cd 45%,#d9dfe4 70%,#a9b4bf 100%)}
.hero .photo{position:absolute;inset:0}
.hero .inner{position:absolute;left:0;right:0;top:230px;text-align:center;color:var(--white)}
.hero h1{font-family:var(--head);font-weight:700;font-size:56px;text-shadow:0 2px 6px rgba(0,0,0,.25)}
.hero p{font-size:19px;margin:18px 0 38px;text-shadow:0 1px 4px rgba(0,0,0,.35)}
.hero .btn{font-size:20px;padding:16px 44px}
.hero svg.curve{position:absolute;left:0;bottom:0}

/* welcome */
.welcome{height:570px;display:flex;padding:0 90px}
.welcome .text{width:480px;padding-top:115px}
.welcome h2{font-family:var(--head);font-size:38px;color:var(--navy);font-weight:700;margin-bottom:40px}
.welcome p{font-size:16px;line-height:1.6;color:var(--navy);margin-bottom:30px}
.welcome .art{position:absolute;left:730px;top:105px}

/* services */
.services{height:700px;background:var(--grey-bg);text-align:center}
.section-title{font-family:var(--head);font-weight:700;font-size:38px;color:var(--navy)}
.services .section-title{padding-top:65px}
.cards{position:absolute;left:93px;top:167px;display:flex}
.card{width:254px;color:var(--white);text-align:center;padding:40px 22px 0}
.card.orange{background:var(--orange);height:370px;margin-top:28px}
.card.blue{background:var(--navy);height:370px}
.card svg{display:block;margin:0 auto 18px}
.card h3{font-family:var(--head);font-size:23px;font-weight:700;margin-bottom:12px}
.card p{font-size:15px;line-height:1.4;margin-bottom:18px}
.card .pill{display:inline-block;border:1.5px solid var(--white);border-radius:20px;font-size:13px;padding:6px 18px}
.arrow{position:absolute;width:40px;height:40px;border-radius:50%;background:#111;display:flex;align-items:center;justify-content:center}

/* savings */
.savings{height:665px;background:linear-gradient(180deg,#27282b,#151517);color:var(--white);text-align:center}
.savings h2{font-family:var(--head);font-size:40px;font-weight:700;padding-top:60px}
.savings .lead{font-size:18px;margin-top:20px}
.savings ul{position:absolute;top:215px;list-style:none;text-align:left;font-size:16px;line-height:1.5}
.savings li{position:relative;padding-left:30px;margin-bottom:42px}
.savings li::before{content:"";position:absolute;left:0;top:10px;width:6px;height:6px;border-radius:50%;background:var(--white)}
.savings .col1{left:170px;width:470px}
.savings .col2{left:820px;width:340px}
.savings .btn{position:absolute;left:520px;top:565px}

/* partners */
.partners{height:525px;text-align:center}
.partners .section-title{padding-top:90px}
.partners p{font-size:17px;line-height:1.5;margin-top:28px}
.logos{position:absolute;top:290px;left:80px;display:flex;gap:26px}
.logo-box{width:240px;height:168px;background:var(--white);box-shadow:0 2px 10px rgba(0,0,0,.35);display:flex;align-items:center;justify-content:center}
.logo-box span{display:block;width:140px;height:70px;border-radius:6px;background:#d9dce3}

/* testimonials */
.testimonials{height:500px;background:#eeeeee;text-align:center}
.testimonials .map{position:absolute;left:170px;top:30px;width:860px;height:420px;background:radial-gradient(ellipse at center,#dcdcdc 0%,#eeeeee 70%)}
.testimonials .section-title{position:relative;padding-top:70px;font-size:40px}
.quote{position:relative;width:960px;margin:52px auto 0;font-size:15px;line-height:2;color:var(--ink)}
.quote .mk{font-size:30px;font-family:Georgia,serif;color:var(--navy);line-height:0}
.signature{position:relative;margin:28px auto 0;width:140px;height:40px;background:#d0d0d0;border-radius:20px}
.quote-name{position:relative;margin-top:18px;font-size:16px}

/* cta */
.cta{height:400px;background:var(--grey-bg);text-align:center;color:var(--navy)}
.cta h2{font-family:var(--head);font-size:40px;font-weight:600;padding-top:80px}
.cta .sub{font-size:29px;margin-top:22px}
.cta .tag{font-size:29px;margin-top:18px}
.cta .btn{margin-top:36px;font-size:16px;padding:12px 32px}

/* contact info */
.contact-info{height:640px}
.person{position:absolute;left:440px;top:35px;width:330px;height:340px;background:linear-gradient(180deg,#d6d9de,#9aa2ad)}
.info-row{position:absolute;left:93px;top:365px;width:1014px;height:270px;background:var(--white);border:1px solid #ddd;display:flex;text-align:center}
.info{flex:1;padding-top:30px;border-right:1px solid #ddd}
.info:last-child{border-right:0}
.info svg{display:block;margin:0 auto 12px}
.info h3{font-family:var(--head);font-size:27px;font-weight:500;margin-bottom:12px}
.info p{font-size:15px;line-height:1.6}

/* footer */
.site-footer{height:477px;background:#000;color:var(--white)}
.site-footer svg.top{position:absolute;left:0;top:-1px}
.foot-brand{position:absolute;left:90px;top:175px;font-family:var(--head);font-weight:700;font-size:30px;display:flex;align-items:center;gap:14px}
.foot-brand .mark{width:26px;height:26px;background:var(--white);border-radius:50%}
.fcol{position:absolute;top:30px;font-size:15px;line-height:1.9}
.fcol h4{font-family:var(--head);font-size:18px;font-weight:700;margin-bottom:14px}
.fcol.links{left:460px}
.fcol.serv{left:645px}
.fcol.news{left:860px;width:250px;line-height:1.5}
.news input{display:block;width:240px;height:32px;margin:20px 0 12px;border:0;padding:0 8px;font-size:12px;font-family:var(--body)}
.news .btn{font-size:14px;padding:8px 26px;border-radius:18px}
.copyright{position:absolute;left:90px;top:418px;font-size:13px}
.foot-social{position:absolute;right:90px;top:408px;display:flex;gap:8px}
.foot-social span{width:24px;height:24px;background:var(--white);border-radius:3px}
</style>
</head>
<body>

<div class="topbar">
  <div class="item">
    <svg width="16" height="22" viewBox="0 0 16 22"><path d="M8 0a8 8 0 0 1 8 8c0 6-8 14-8 14S0 14 0 8a8 8 0 0 1 8-8z" fill="#fff"/><circle cx="8" cy="8" r="3" fill="#f26a1b"/></svg>
    <span>12 Harlow Lane, Brightmere QLD 4000</span>
  </div>
  <div class="item">
    <svg width="18" height="18" viewBox="0 0 18 18"><path d="M4 1l3 4-2 2c1 3 3 5 6 6l2-2 4 3-2 3C8 17 1 10 1 3z" fill="#fff"/></svg>
    <span>1300-000-123</span>
  </div>
  <div class="item">
    <svg width="20" height="14" viewBox="0 0 20 14"><rect x="1" y="1" width="18" height="12" fill="none" stroke="#fff" stroke-width="1.6"/><path d="M1 1l9 7 9-7" fill="none" stroke="#fff" stroke-width="1.6"/></svg>
    <span>info@tvkb-example.net</span>
  </div>
  <div class="social" aria-label="Social links"><span></span><span></span><span></span><span></span></div>
</div>

<header class="site-header">
  <div class="brand"><span class="mark"></span>Tidewell Systems</div>
  <nav class="nav">
    <a>Home</a><a>Our Services</a><a>About Us</a><a>Our Team</a><a>Contact Us</a><a>Support</a>
  </nav>
</header>

<section class="hero">
  <div class="photo" role="img" aria-label="Photo of a doctor in a white coat holding a tablet in a bright clinic"></div>
  <div class="inner">
    <h1>Welcome to Tidewell Systems!</h1>
    <p>A Better Tomorrow, Through Intelligent use of Technology Today!</p>
    <a class="btn">View More</a>
  </div>
  <svg class="curve" width="1200" height="60" viewBox="0 0 1200 60" preserveAspectRatio="none">
    <path d="M0 20 Q600 75 1200 10 L1200 60 L0 60z" fill="#fff"/>
    <path d="M0 20 Q600 75 1200 10" fill="none" stroke="#1f2a78" stroke-width="8"/>
  </svg>
</section>

<section class="welcome">
  <div class="text">
    <h2>Welcome to our website!</h2>
    <p>Welcome to Tidewell Systems where we believe that a better tomorrow, starts through intelligent use of technology today! Tidewell Systems is a valued added information technology company supplying and implementing hardware and software.</p>
    <a class="btn">Read More</a>
  </div>
  <svg class="art" width="380" height="380" viewBox="0 0 380 380">
    <path d="M210 10 A170 170 0 0 1 370 230 L300 200 A100 100 0 0 0 220 80z" fill="#f26a1b"/>
    <polygon role="img" aria-label="Photo of a team meeting around a desk seen from above" points="190,20 335,105 335,275 190,360 45,275 45,105" fill="#b9c3cf"/>
  </svg>
</section>

<section class="services">
  <h2 class="section-title">Our Services</h2>
  <div class="arrow" style="left:25px;top:383px"><svg width="14" height="14" viewBox="0 0 14 14"><path d="M10 1L3 7l7 6z" fill="#fff"/></svg></div>
  <div class="cards">
    <div class="card orange">
      <svg width="48" height="44" viewBox="0 0 48 44"><rect x="3" y="3" width="42" height="28" rx="2" fill="none" stroke="#fff" stroke-width="2.5"/><path d="M18 40h12M24 31v9" stroke="#fff" stroke-width="2.5"/></svg>
      <h3>Software</h3>
      <p>Tidewell Systems has the tools, capabilities and expertise to guide any organisation with their software requirements</p>
      <span class="pill">Read More</span>
    </div>
    <div class="card blue">
      <svg width="48" height="44" viewBox="0 0 48 44"><rect x="6" y="4" width="36" height="16" rx="2" fill="none" stroke="#fff" stroke-width="2.5"/><path d="M4 40c6-10 14-10 20-6 6-4 14-4 20 6" fill="none" stroke="#fff" stroke-width="2.5"/></svg>
      <h3>Products</h3>
      <p>We will determine and provide appropriate products and services to address your technology requirements</p>
      <span class="pill">Read More</span>
    </div>
    <div class="card orange">
      <svg width="48" height="44" viewBox="0 0 48 44"><circle cx="16" cy="16" r="9" fill="none" stroke="#fff" stroke-width="2.5"/><circle cx="33" cy="28" r="9" fill="none" stroke="#fff" stroke-width="2.5"/></svg>
      <h3>Solutions</h3>
      <p>A full range of IT Solutions, includes carefully selected IT Service Partners to minimize risk and improve continuity</p>
      <span class="pill">Read More</span>
    </div>
    <div class="card blue">
      <svg width="48" height="44" viewBox="0 0 48 44"><rect x="10" y="2" width="28" height="12" fill="none" stroke="#fff" stroke-width="2.5"/><rect x="3" y="14" width="42" height="18" rx="2" fill="none" stroke="#fff" stroke-width="2.5"/><rect x="10" y="28" width="28" height="14" fill="none" stroke="#fff" stroke-width="2.5"/></svg>
      <h3>Copiers</h3>
      <p>B&amp;W Photocopiers &amp; RIP with full integration into networks for printing and scanning</p>
      <span class="pill">Read More</span>
    </div>
  </div>
  <div class="arrow" style="left:1135px;top:383px"><svg width="14" height="14" viewBox="0 0 14 14"><path d="M4 1l7 6-7 6z" fill="#fff"/></svg></div>
</section>

<section class="savings">
  <h2>How we can save you $$$</h2>
  <p class="lead">We pride ourselves in offering only the best solutions, with our diverse skill set in areas including:</p>
  <ul class="col1">
    <li>Medical Software including ClinicDesk, PracFlow and CareLedger. We can also assist with eHealth incentive compliance</li>
    <li>Terminal Services/RDP connections</li>
    <li>NAS installations</li>
    <li>Cloud based solutions</li>
    <li>Data recovery</li>
  </ul>
  <ul class="col2">
    <li>Legal packages including LexNote</li>
    <li style="margin-top:42px">Mail server hosting</li>
    <li style="margin-top:78px">Virtualisation</li>
    <li>Virus prevention and removal</li>
  </ul>
  <a class="btn">Read More</a>
</section>

<section class="partners">
  <h2 class="section-title">Some of our Partners</h2>
  <p>We Partner With Only The Best Companies Around The World To Offer Our Clients<br>The Best In Hardware And Software Solutions</p>
  <div class="arrow" style="left:25px;top:355px"><svg width="14" height="14" viewBox="0 0 14 14"><path d="M10 1L3 7l7 6z" fill="#fff"/></svg></div>
  <div class="logos">
    <div class="logo-box"><span></span></div>
    <div class="logo-box"><span></span></div>
    <div class="logo-box"><span></span></div>
    <div class="logo-box"><span></span></div>
  </div>
  <div class="arrow" style="left:1135px;top:355px"><svg width="14" height="14" viewBox="0 0 14 14"><path d="M4 1l7 6-7 6z" fill="#fff"/></svg></div>
</section>

<section class="testimonials">
  <div class="map" role="img" aria-label="Faint dotted world map in the background"></div>
  <h2 class="section-title">Testimonials</h2>
  <div class="arrow" style="left:25px;top:235px"><svg width="14" height="14" viewBox="0 0 14 14"><path d="M10 1L3 7l7 6z" fill="#fff"/></svg></div>
  <p class="quote"><span class="mk">&ldquo;</span> Tidewell Systems have saved us time, money and stress by implementing technology solutions for our business computer requirements. Problems we have experienced with any of our existing software or hardware applications have been dealt with in a professional, speedy and pleasant manner, whether attended by Sam or by any one of his skilled team. <span class="mk">&rdquo;</span></p>
  <div class="signature" role="img" aria-label="Handwritten signature"></div>
  <p class="quote-name">Dana and Kit Morrow</p>
  <div class="arrow" style="left:1135px;top:235px"><svg width="14" height="14" viewBox="0 0 14 14"><path d="M4 1l7 6-7 6z" fill="#fff"/></svg></div>
</section>

<section class="cta">
  <h2>Tidewell Systems</h2>
  <p class="sub">We are here to help you!</p>
  <p class="tag">A Better Tomorrow, Through Intelligent use of Technology Today</p>
  <a class="btn">Contact Us</a>
</section>

<section class="contact-info">
  <div class="person" role="img" aria-label="Photo of a smiling businessman holding a tablet and giving a thumbs up"></div>
  <div class="info-row">
    <div class="info">
      <svg width="56" height="62" viewBox="0 0 56 62"><rect x="6" y="3" width="44" height="56" rx="3" fill="none" stroke="#1f2a78" stroke-width="3"/><circle cx="28" cy="24" r="7" fill="none" stroke="#1f2a78" stroke-width="3"/><path d="M16 46c2-8 22-8 24 0" fill="none" stroke="#1f2a78" stroke-width="3"/></svg>
      <h3>Address info</h3>
      <p>12 Harlow Lane, Brightmere<br>QLD 4000</p>
    </div>
    <div class="info">
      <svg width="66" height="62" viewBox="0 0 66 62"><circle cx="30" cy="30" r="26" fill="none" stroke="#f26a1b" stroke-width="3"/><circle cx="30" cy="24" r="7" fill="none" stroke="#f26a1b" stroke-width="3"/><path d="M18 44c3-8 21-8 24 0" fill="none" stroke="#f26a1b" stroke-width="3"/></svg>
      <h3>Working hours</h3>
      <p>Monday – Friday 8 AM – 5<br>PM</p>
    </div>
    <div class="info">
      <svg width="56" height="62" viewBox="0 0 56 62"><path d="M10 30a18 18 0 0 1 36 0" fill="none" stroke="#1f2a78" stroke-width="4"/><rect x="6" y="28" width="9" height="16" rx="3" fill="#1f2a78"/><rect x="41" y="28" width="9" height="16" rx="3" fill="#1f2a78"/><circle cx="28" cy="30" r="9" fill="#1f2a78"/><path d="M12 58c2-10 30-10 32 0" fill="#1f2a78"/></svg>
      <h3>Support center</h3>
      <p>Our team are ready and<br>waiting to assist you with all<br>your Information Technology<br>requirements.</p>
    </div>
  </div>
</section>

<footer class="site-footer">
  <svg class="top" width="1200" height="40" viewBox="0 0 1200 40" preserveAspectRatio="none"><path d="M0 0h1200v4Q600 40 0 4z" fill="#fff"/></svg>
  <div class="fcol links">
    <h4>Quick Links</h4>
    <p>Home<br>Our Services<br>About Us<br>Our Team<br>Contact Us<br>Support</p>
  </div>
  <div class="fcol serv">
    <h4>Services</h4>
    <p>Software<br>Products<br>Solutions<br>Programming<br>Copiers<br>Printers &amp; Scanners</p>
  </div>
  <div class="fcol news">
    <h4>Newsletter</h4>
    <p>A Better Tomorrow, through intelligent use of Technology Today</p>
    <input type="email" placeholder="Enter the Email">
    <a class="btn">Send</a>
  </div>
  <div class="foot-brand"><span class="mark"></span>Tidewell Systems</div>
  <p class="copyright">Copyright © 2019 Tidewell Systems</p>
  <div class="foot-social" aria-label="Social links"><span></span><span></span><span></span><span></span></div>
</footer>

</body>
</html>
```